Supplier to the Wide Format Print Industry requires a modern and informative business card design

Our supply business has a dual focus to be represented on each side of the business card. KV Depot supplies large format print materials, hardware, inks & maintenance services. We are also the Velmar Coastal product distributor for Queensland and Northern NSW. Seeking a modern design.

Target Market(s)

Sign Makers, Government, Plan printers, Designers

Contact Information for Business Card

KV Depot side
Neil Fansworth - General Manager
M 0427 916 204
1300 652 318
neil@kvdepot-example.com.au
14 Colvin Tarr Street, Burleigh Heads, Qld, 4220
www.kvdepot-example.com.au

Colors

Designer to choose colors to be used in the design.

Requirements
Must have
• Modern/Creative flavour
• Side 2. Large Velmar logo with footnote ......
• Queensland and Northern NSW Distributor
• 14 Colvin Tarr Street, Burleigh Heads, Qld, 4220
• 1300 652 318
Nice to have
• Impress me

```html
<!DOCTYPE html>
<html lang="en">
<head>
<meta charset="utf-8">
<title>KV Depot – Business Card</title>
<link href="https://fonts.googleapis.com/css2?family=Open+Sans:wght@400;600;700&display=swap" rel="stylesheet">
<style>
  :root {
    --backdrop: #2a0004;
    --card-white: #ffffff;
    --brand-red: #c0282d;
    --deep-red: #a8222b;
    --glow-red: #e2695f;
    --ink: #2b2b2b;
    --rule-grey: #d9d9d9;
    --icon-red: #e8564f;
    --white: #ffffff;
  }
  * { margin: 0; padding: 0; box-sizing: border-box; }
  html, body {
    width: 1200px; height: 900px; overflow: hidden;
    background: var(--backdrop);
    font-family: "Open Sans", Arial, sans-serif;
  }
  .canvas { position: relative; width: 1200px; height: 900px; }

  .card { position: absolute; width: 477px; height: 293px; overflow: hidden; }

  /* Front: KV Depot */
  .card-front {
    left: 120px; top: 275px;
    background: var(--card-white);
    border-radius: 0 56px 0 56px;
  }
  .brand-block { position: absolute; left: 225px; top: 60px; width: 219px; }
  .brand-name {
    display: flex; align-items: center; gap: 10px;
    font-size: 38px; font-weight: 700; line-height: 1;
    color: var(--brand-red); letter-spacing: -0.5px;
  }
  .brand-mark { width: 18px; height: 18px; background: var(--brand-red); }
  .brand-tagline {
    margin-top: 10px; font-size: 12px; font-weight: 700; color: #111;
    line-height: 1.1; padding-bottom: 3px;
    border-bottom: 2px solid #111;
  }
  .brand-tagline span { display: block; font-size: 10px; }

  .person { position: absolute; left: 30px; top: 159px; width: 414px; }
  .person-name {
    font-size: 17px; font-weight: 400; color: var(--brand-red);
    letter-spacing: 0.4px; line-height: 1.1;
  }
  .person-role {
    display: flex; align-items: center; gap: 6px;
    font-size: 12.5px; color: var(--ink); margin-top: 2px;
  }
  .person-role::after {
    content: ""; flex: 1; height: 1px; background: var(--rule-grey);
  }

  .address {
    position: absolute; left: 32px; top: 236px;
    font-size: 12px; font-style: normal; color: var(--ink); line-height: 17px;
  }
  .contacts {
    position: absolute; right: 32px; top: 200px;
    list-style: none; text-align: right;
    font-size: 12px; color: var(--ink); line-height: 17.5px;
  }
  .contacts li { display: flex; align-items: center; justify-content: flex-end; gap: 3px; white-space: nowrap; }
  .contacts svg { width: 10px; height: 10px; fill: var(--icon-red); }

  /* Back: Velmar Coastal */
  .card-back {
    left: 606px; top: 274px;
    border-radius: 56px 0 56px 0;
    background: radial-gradient(ellipse 60% 65% at 50% 40%, var(--glow-red) 0%, #c8383a 55%, var(--deep-red) 100%);
    box-shadow: 4px 5px 8px rgba(0,0,0,0.55);
    color: var(--white); text-align: center;
  }
  .partner-mark {
    position: absolute; left: 197px; top: 54px;
    width: 84px; height: 84px; border-radius: 50%;
    background: rgba(255,255,255,0.9);
  }
  .partner-name {
    position: absolute; left: 0; right: 0; top: 148px;
    font-size: 30px; font-weight: 700; line-height: 1; letter-spacing: -0.5px;
  }
  .partner-tagline {
    position: absolute; left: 0; right: 0; top: 189px;
    font-size: 8.5px; line-height: 10px; letter-spacing: 0.3px; text-transform: uppercase;
  }
  .partner-rule {
    position: absolute; left: 89px; width: 301px; top: 219px;
    height: 1px; background: rgba(255,255,255,0.5);
  }
  .partner-role {
    position: absolute; left: 0; right: 0; top: 226px;
    font-size: 13px; font-weight: 600; letter-spacing: 0.2px;
  }
</style>
</head>
<body>
<main class="canvas">

  <section class="card card-front" aria-label="KV Depot business card front">
    <div class="brand-block">
      <div class="brand-name">KV Depot<span class="brand-mark"></span></div>
      <div class="brand-tagline"><span>large format</span>digital printing supplies</div>
    </div>

    <div class="person">
      <p class="person-name">NEIL FANSWORTH</p>
      <p class="person-role">General Manager</p>
    </div>

    <ul class="contacts">
      <li>1300 652 318
        <svg viewBox="0 0 10 10" aria-hidden="true"><path d="M1 3.5C1 2 2.5 1.5 5 1.5S9 2 9 3.5L7.2 4 6.8 3H3.2L2.8 4zM2.5 5h5l1 3.5h-7z"/></svg>
      </li>
      <li>0427 916 204
        <svg viewBox="0 0 10 10" aria-hidden="true"><path d="M3 0.5h4a.8.8 0 0 1 .8.8v7.4a.8.8 0 0 1-.8.8H3a.8.8 0 0 1-.8-.8V1.3A.8.8 0 0 1 3 .5zm.4 1.2v6h3.2v-6zM5 8a.4.4 0 1 0 0 .01z"/></svg>
      </li>
      <li>neil@kvdepot-example.com.au
        <svg viewBox="0 0 10 10" aria-hidden="true"><path d="M0.5 2h9v6h-9zM1.2 2.6 5 5.6l3.8-3z" fill-rule="evenodd"/></svg>
      </li>
      <li>www.kvdepot-example.com.au
        <svg viewBox="0 0 10 10" aria-hidden="true"><circle cx="5" cy="5" r="4.5"/></svg>
      </li>
    </ul>

    <address class="address">
      14 Colvin Tarr Street,<br>
      Burleigh Heads, Qld, 4220
    </address>
  </section>

  <section class="card card-back" aria-label="Velmar Coastal distributor card back">
    <div class="partner-mark" aria-hidden="true"></div>
    <p class="partner-name">Velmar Coastal</p>
    <p class="partner-tagline">Large format printing materials<br>&amp; industrial fabrics</p>
    <div class="partner-rule"></div>
    <p class="partner-role">Distributor for&nbsp; Queensland and Northern NSW</p>
  </section>

</main>
</body>
</html>
```